A5 flyer required for motorcycle tracking device - Easy.

We are a UK company who supply pizza delivery bikes, we now also supply "Motorcycle tracking devices"..
We want the flyer to be in similiar style to that of our new to be website design so that there is consistancy throughout.
Updates

Project Deadline Extended
Reason: Extended due to information not being present - my mistake apologies!

Hi Designers!

Please use the "Velluto pizza" delivery bike as supplied in the brief (Blue bike with box on), if you require a different image etc just let me know & I`ll upload. Also somewhere on the flyer this information needs to be added..

"Kit consists: Motorcycle Tracker
                    Internal battery
                    Connection leads
                    Full Instructions"

Just so they understand what it is that they are purchasing......Thank You!

Target Market(s)

Owners and managers more importantly these people loose revenue from stolen bikes,mostly males between age of 30 to 50

Industry/Entity Type

Pizza Delivery

Requirements
Must have
• One single side in colour must incorporate an image of the QR240-7K motorcycle that we sell but only as a small feature which could be part of an easy step guide, the emphassis needs to be on the tracker itself.
• All the bullet points listed in the word doc uploaded. Maybe one hard hitting line to head like "Purchasing this could seriously protect your wealth"...sort of thing, you get the idea.
• Reference to www.ridecrate.example.co.uk as shown and in the same design/font on our website but as the new homepage design
Nice to have
• Would be nice if the customer could see in easy steps how the tracker would intergrate with their current motorcycle ie, Purchase tracker from us, Insert PAYG sim card, Install tracker into motorcycle (Just 2 wires required)...then track their asset(Motorcycle) with their mobile phone (Preferable) or internet

```html
<!DOCTYPE html>
<html lang="en">
<head>
<meta charset="utf-8">
<title>Track your motorcycle – RideCrate tracker flyer</title>
<link href="https://fonts.googleapis.com/css2?family=PT+Sans:ital,wght@0,400;0,700;1,400;1,700&display=swap" rel="stylesheet">
<style>
  :root {
    --bg: #1c1c1c;
    --white: #f4f4f4;
    --gold: #f2aa1e;
    --gold-deep: #d98a0c;
    --device: #2a2d33;
    --sim: #c9c9c9;
    --bike-blue: #1f4fc8;
  }
  * { margin: 0; padding: 0; box-sizing: border-box; }
  html, body { width: 846px; height: 1200px; overflow: hidden; background: var(--bg); }
  .flyer {
    position: relative; width: 846px; height: 1200px; background: var(--bg);
    font-family: "PT Sans", "Myriad Pro", Arial, sans-serif; color: var(--white); font-weight: 700;
  }
  .flyer > * { position: absolute; }
  .gold { color: var(--gold); }

  .site-url { left: 22px; top: 16px; font-size: 24px; letter-spacing: 0.2px; }
  .offer { right: 14px; top: 14px; text-align: right; }
  .offer-title { font-size: 25px; color: var(--gold); line-height: 1.1; }
  .offer-terms { font-size: 16px; line-height: 1.2; margin-top: 4px; text-align: center; }

  .headline { left: 0; width: 846px; top: 84px; text-align: center; font-size: 62px; line-height: 1.0; }
  .headline .track { background: linear-gradient(var(--gold), var(--gold-deep)); -webkit-background-clip: text; background-clip: text; color: transparent; }
  .headline-sub { left: 0; width: 846px; top: 212px; text-align: center; font-size: 25px; color: var(--gold); }

  .step { display: flex; align-items: center; gap: 8px; }
  .step-num { font-size: 72px; font-style: italic; line-height: 1; color: var(--gold); }
  .step-text { font-size: 30px; line-height: 1.05; }
  .step-text small { display: block; font-size: 15px; color: var(--gold); text-align: center; }

  .step-sim { left: 104px; top: 268px; }
  .step-install { left: 500px; top: 430px; }
  .step-track { left: 100px; top: 610px; }

  .sim-visual { left: 532px; top: 284px; width: 130px; height: 66px; background: linear-gradient(160deg, #e0e0e0, var(--sim)); border-radius: 4px; }
  .device-visual { left: 169px; top: 400px; width: 206px; height: 130px; background: linear-gradient(170deg, #3a3e45, var(--device)); border-radius: 8px; }
  .device-caption { left: 169px; top: 550px; width: 206px; text-align: center; font-size: 12px; color: var(--gold); line-height: 1.25; }

  .battery { left: 600px; top: 524px; text-align: center; font-size: 16px; font-style: italic; line-height: 1.3; }
  .battery span { color: var(--gold); font-size: 17px; }

  .tagline { left: 0; width: 846px; top: 740px; text-align: center; font-size: 28px; font-style: italic; }
  .bike-visual { left: 302px; top: 810px; width: 230px; height: 158px; background: radial-gradient(ellipse at 50% 55%, var(--bike-blue), #152a5a 60%, var(--bg) 80%); border-radius: 40px; }
  .bike-model { left: 546px; top: 905px; font-size: 17px; }

  .enquiries { left: 0; width: 846px; top: 986px; text-align: center; font-size: 32px; line-height: 1.25; }
  .enquiries .phone { color: var(--gold); font-size: 34px; }

  .running-cost { left: 0; width: 846px; top: 1126px; text-align: center; font-size: 27px; font-style: italic; }
  .footnote { left: 0; width: 846px; top: 1163px; text-align: center; font-size: 11px; font-style: italic; color: var(--gold); }
</style>
</head>
<body>
<main class="flyer">
  <div class="site-url">WWW.RIDECRATE.EXAMPLE.CO.UK</div>

  <div class="offer">
    <div class="offer-title">No yearly subscription!</div>
    <div class="offer-terms">One off fee of £125 per tracker +<br>£10 per PAYG SIM card</div>
  </div>

  <h1 class="headline"><span class="track">Track</span> your<br>motorcycle!</h1>
  <div class="headline-sub">in 3 easy steps</div>

  <div class="step step-sim"><span class="step-num">1</span><span class="step-text">insert the PAYG sim card</span></div>
  <div class="sim-visual" role="img" aria-label="PAYG SIM card"></div>

  <div class="device-visual" role="img" aria-label="Black motorcycle tracker unit with three indicator lights"></div>
  <div class="device-caption">Small size 9cm H 5cm W 2cm D,<br>can easily be hidden.</div>

  <div class="step step-install"><span class="step-num">2</span><span class="step-text">install our device<small>with just 2 wires!</small></span></div>
  <div class="battery">Battery lasts up to<br><span>14 hours!</span></div>

  <div class="step step-track"><span class="step-num">3</span><span class="step-text">start tracking!<small>on your phone!</small></span></div>

  <p class="tagline">Can you seriously afford <span class="gold">not</span> to be without one of these?</p>

  <div class="bike-visual" role="img" aria-label="Blue delivery scooter with a top box"></div>
  <div class="bike-model">QR240-7K</div>

  <p class="enquiries">Enquires will be answered immediately on<br><span class="phone">07700 900481.</span></p>

  <p class="running-cost">As little as <span class="gold">40p per year</span> to use/ maintain!*</p>
  <p class="footnote">*(SIM card requires 1 use, 1 txt per 3 months to remain active)</p>
</main>
</body>
</html>
```